Logo + Label Design (Men’s Grooming Brand & Product Packaging)

Design a logo and 2 oz pomade label for Brant, a modern men’s grooming brand focused on clean, high-quality, natural ingredients. The design should establish a bold, masculine, minimalist identity that can later extend to products like shaving gel and body wash.

Key Requirements

Create a primary logo for “Brant” and a core label for the 2 oz pomade jar (screw-top).

Use a clean, modern style — masculine, confident, and approachable (think Wendel’s, Valto, Northfield Mill).

Design for 1–2 color screen printing on solid jar colors (white, black, or navy).

Avoid gradients, foil, or embossing. Must work in black & white.

Provide: vector logo, mockup of the 2 oz jar, color palette (CMYK/RGB/HEX), and font specs.

Winning design may lead to future projects (body wash, shave gel, skincare lines).

Font styles to use
Other font styles liked:
• We like the fonts and design concept in the attached mockup.

Requirements
Should not have
• We want to avoid too much writing or busy designs. We want to avoid having graphics/illustrations embedded in the logo if they will cause the brand to look less classy or sophisticated. We also want the design to look simple and all-American (e.g. Pellham and Stroud, Tall Pine, The BRIM, etc). We’d like to give a Kessler & Dunmore vibe that feels classy and high end.

```html
<!DOCTYPE html>
<html lang="en">
<head>
<meta charset="utf-8">
<title>Brant Hair Pomade – Colorways</title>
<link href="https://fonts.googleapis.com/css2?family=Montserrat:wght@400;500;700;800&display=swap" rel="stylesheet">
<style>
  :root {
    --bg-stone: #2b2d2a;
    --bg-frost: #cfced4;
    --bg-onyx: #151515;
    --bg-navy: #0e2456;
    --jar-stone: #7e7f79;
    --jar-frost: #eef0f3;
    --jar-onyx: #1d1d1e;
    --jar-navy: #1f4fa8;
    --ink-light: #ffffff;
    --ink-dark: #141416;
    --accent-tan: #c9a58c;
    --accent-soft: #8a8a90;
    --accent-sky: #c9d6ef;
  }
  * { box-sizing: border-box; margin: 0; padding: 0; }
  html, body { width: 1200px; height: 854px; overflow: hidden; }
  body {
    font-family: "Montserrat", sans-serif;
    display: grid;
    grid-template-columns: 600px 600px;
    grid-template-rows: 427px 427px;
  }
  .colorway {
    display: flex;
    flex-direction: column;
    align-items: center;
    justify-content: center;
    gap: 18px;
    color: var(--ink);
  }
  .colorway--stone { background: var(--bg-stone); --jar: var(--jar-stone); --ink: var(--ink-light); --accent: var(--accent-tan); }
  .colorway--frost { background: var(--bg-frost); --jar: var(--jar-frost); --ink: var(--ink-dark); --accent: var(--accent-soft); }
  .colorway--onyx  { background: var(--bg-onyx);  --jar: var(--jar-onyx);  --ink: var(--ink-light); --accent: var(--accent-tan); }
  .colorway--navy  { background: var(--bg-navy);  --jar: var(--jar-navy);  --ink: var(--ink-light); --accent: var(--accent-sky); }

  .lid-label {
    width: 200px; height: 200px;
    border-radius: 50%;
    background: var(--jar);
    display: flex; flex-direction: column; align-items: center;
    padding-top: 26px;
  }
  .brand-name { font-weight: 800; font-size: 34px; letter-spacing: -0.5px; line-height: 1; }
  .product-name { font-weight: 800; font-size: 16px; letter-spacing: 2px; margin-top: 20px; }
  .scent { font-weight: 700; font-size: 11px; margin-top: 4px; }
  .spec { font-weight: 500; font-size: 7px; letter-spacing: 0.3px; color: var(--accent); margin-top: 12px; }
  .net-weight { font-weight: 400; font-size: 9px; margin-top: 14px; display: flex; align-items: baseline; gap: 3px; }
  .net-weight .estimated { font-size: 17px; line-height: 1; }
  .net-weight .metric { font-size: 7px; }

  .side-label {
    width: 182px; height: 66px;
    border-radius: 4px;
    background: var(--jar);
    padding: 10px 10px 0 40px;
    display: flex; flex-direction: column;
  }
  .side-label .brand-name { font-size: 14px; }
  .side-label .product-name { font-size: 8.5px; margin-top: 4px; letter-spacing: 1.3px; }
  .side-label .scent { font-size: 6.5px; margin-top: 2px; }
  .side-label .rule { display: flex; justify-content: space-between; align-items: center; border-top: 0.5px solid var(--accent); margin-top: 4px; padding-top: 2px; font-size: 4.5px; font-weight: 700; letter-spacing: 0.6px; color: var(--accent); }
</style>
</head>
<body>
  <section class="colorway colorway--stone">
    <div class="lid-label">
      <div class="brand-name">Brant.</div>
      <div class="product-name">HAIR POMADE</div>
      <div class="scent">FRESH &amp; CLEAN</div>
      <div class="spec">MEDIUM HOLD | MATTE FINISH</div>
      <div class="net-weight"><span class="estimated">℮</span>2 oz | <span class="metric">57 g</span></div>
    </div>
    <div class="side-label">
      <div class="brand-name">Brant.</div>
      <div class="product-name">HAIR POMADE</div>
      <div class="scent">FRESH &amp; CLEAN</div>
      <div class="rule"><span>MEDIUM HOLD | MATTE FINISH</span><span>℮ 2 oz</span></div>
    </div>
  </section>

  <section class="colorway colorway--frost">
    <div class="lid-label">
      <div class="brand-name">Brant.</div>
      <div class="product-name">HAIR POMADE</div>
      <div class="scent">FRESH &amp; CLEAN</div>
      <div class="spec">MEDIUM HOLD | MATTE FINISH</div>
      <div class="net-weight"><span class="estimated">℮</span>2 oz | <span class="metric">57 g</span></div>
    </div>
    <div class="side-label">
      <div class="brand-name">Brant.</div>
      <div class="product-name">HAIR POMADE</div>
      <div class="scent">FRESH &amp; CLEAN</div>
      <div class="rule"><span>MEDIUM HOLD | MATTE FINISH</span><span>℮ 2 oz</span></div>
    </div>
  </section>

  <section class="colorway colorway--onyx">
    <div class="lid-label">
      <div class="brand-name">Brant.</div>
      <div class="product-name">HAIR POMADE</div>
      <div class="scent">FRESH &amp; CLEAN</div>
      <div class="spec">MEDIUM HOLD | MATTE FINISH</div>
      <div class="net-weight"><span class="estimated">℮</span>2 oz | <span class="metric">57 g</span></div>
    </div>
    <div class="side-label">
      <div class="brand-name">Brant.</div>
      <div class="product-name">HAIR POMADE</div>
      <div class="scent">FRESH &amp; CLEAN</div>
      <div class="rule"><span>MEDIUM HOLD | MATTE FINISH</span><span>℮ 2 oz</span></div>
    </div>
  </section>

  <section class="colorway colorway--navy">
    <div class="lid-label">
      <div class="brand-name">Brant.</div>
      <div class="product-name">HAIR POMADE</div>
      <div class="scent">FRESH &amp; CLEAN</div>
      <div class="spec">MEDIUM HOLD | MATTE FINISH</div>
      <div class="net-weight"><span class="estimated">℮</span>2 oz | <span class="metric">57 g</span></div>
    </div>
    <div class="side-label">
      <div class="brand-name">Brant.</div>
      <div class="product-name">HAIR POMADE</div>
      <div class="scent">FRESH &amp; CLEAN</div>
      <div class="rule"><span>MEDIUM HOLD | MATTE FINISH</span><span>℮ 2 oz</span></div>
    </div>
  </section>
</body>
</html>
```